Flyer Designer for a Widow and Door Company - loooking for fresh design

We are looking for a flyer designed to advertise our business - we supply and install windows and doors - we are looking for a fresh looking flyer to distribute to drum up business - more information can be found at our website www.brightpanehouse.co.uk - We want a different approach than we currently have - making it vibrant and fresh - you can see the services on the website but its more the graphical design that we are looking for rather than content as the content from the website can be used for each service etc.

Target Market(s)

the general public

Colors

Designer to choose colors to be used in the design.

Requirements
Must have
• vibrant design and images

```html
<!DOCTYPE html>
<html lang="en">
<head>
<meta charset="utf-8">
<title>Bright Pane House – Flyer</title>
<link href="https://fonts.googleapis.com/css2?family=Lato:wght@400;700;900&display=swap" rel="stylesheet">
<style>
:root{
  --stage:#b9bccf;
  --blue:#2f6fb5;
  --blue-dark:#1f3c7c;
  --blue-text:#2563ae;
  --navy-icon:#13258a;
  --ring:#9fcaf3;
  --white:#ffffff;
  --ink:#3a3a3a;
  --brick-1:#7a3a2c;
  --brick-2:#9a4a36;
  --floor:#c9b79e;
  --logo-grey:#5c5c5c;
}
*{box-sizing:border-box;margin:0;padding:0}
html,body{width:1200px;height:1200px;overflow:hidden}
body{background:var(--stage);font-family:"Lato",sans-serif;position:relative}
.flyer{position:absolute;left:159px;top:30px;width:925px;height:1195px;transform:scale(0.954);transform-origin:0 0;background:var(--blue);overflow:hidden;box-shadow:0 6px 18px rgba(0,0,0,.25)}
.abs{position:absolute}
.top-strip{left:0;top:0;width:925px;height:16px;background:var(--blue)}
.hero{left:0;top:16px;width:925px;height:484px;background:linear-gradient(180deg,var(--brick-1) 0%,var(--brick-2) 78%,#b9a48a 86%,var(--floor) 100%)}
.door-open{left:510px;top:30px;width:180px;height:440px;background:linear-gradient(90deg,#dcdcdc,#f2f2f2);}
.doorway{left:345px;top:62px;width:168px;height:385px;background:var(--white);border:6px solid #d9d9d9;text-align:center;padding-top:82px}
.headline{color:var(--blue-text);font-weight:900;line-height:.92;letter-spacing:-.5px}
.headline .l1{font-size:33px}
.headline .l2{font-size:27px}
.headline .l3{font-size:48px}
.headline .l4{font-size:24px}
.headline .l5{font-size:23px}
.call-icon{margin:22px auto 6px;display:block}
.call-number{background:#d3d3d3;color:var(--blue-text);font-weight:900;font-size:21px;padding:6px 0}
.logo-disc{left:-190px;top:-290px;width:530px;height:530px;border-radius:50%;background:var(--white);border:8px solid var(--blue)}
.brand{left:18px;top:70px;display:flex;align-items:center;gap:10px}
.brand-mark{width:30px;height:30px;background:var(--blue-text)}
.brand-name{color:var(--blue-text);font-weight:900;font-size:25px;line-height:1}
.social{left:838px;width:64px;height:64px;border-radius:50%;background:var(--blue);border:4px solid var(--white)}
.window-photo{left:623px;top:340px;width:280px;height:280px;border-radius:50%;border:7px solid var(--white);background:radial-gradient(circle at 45% 40%,#d9a24a 0%,#3d8a8c 40%,#2a6d6e 70%,#7d4c8c 100%)}
.about-tab{left:0;top:462px;width:225px;height:40px;background:var(--white);clip-path:polygon(0 0,190px 0,225px 40px,0 40px)}
.about-title{left:22px;top:466px;color:var(--blue-text);font-weight:900;font-size:27px}
.about-text{left:18px;top:511px;width:600px;color:var(--white);font-size:17px;line-height:21.8px}
.card{top:718px;height:215px;background:var(--white);text-align:center}
.card-ring{top:655px;width:126px;height:126px;border-radius:50%;background:var(--white);border:6px solid var(--ring);display:flex;align-items:center;justify-content:center}
.card-title{color:var(--blue-text);font-weight:900;font-size:18px;margin-top:75px}
.card-text{text-align:left;color:var(--ink);font-size:15.5px;line-height:20px;margin:14px 8px 0 10px}
.benefits{left:22px;top:955px;width:882px;height:118px;border:3px solid var(--white)}
.benefit-col{top:18px;color:var(--white);font-weight:900;font-size:19.5px;line-height:27px;text-transform:uppercase;white-space:nowrap}
.footer{left:0;top:1095px;width:925px;height:100px;background:var(--blue-dark)}
.footer-mark{left:80px;top:18px;width:66px;height:66px;border:3px solid var(--white)}
.footer-address{left:252px;top:14px;color:var(--white);font-size:16px;line-height:18.5px}
.pin{left:-18px;top:22px}
.footer-divider{left:535px;top:15px;width:2px;height:72px;background:var(--white)}
.footer-contact{left:615px;top:14px;color:var(--white);font-size:16px;line-height:18.5px}
.footer-contact svg{position:absolute;left:-24px}
</style>
</head>
<body>
<div class="flyer">
  <div class="abs top-strip"></div>
  <div class="abs hero" role="img" aria-label="Photo of a red brick interior wall with wooden floor and an open white front door"></div>
  <div class="abs door-open" role="img" aria-label="Open white panelled door with oval glass window"></div>

  <div class="abs doorway">
    <div class="headline">
      <div class="l1">WE CAN</div>
      <div class="l2">HELP YOU</div>
      <div class="l3">PIECE</div>
      <div class="l4">TOGETHER</div>
      <div class="l5">A SOLUTION</div>
    </div>
    <svg class="call-icon" width="40" height="40" viewBox="0 0 40 40">
      <circle cx="20" cy="20" r="18" fill="#2563ae"/>
      <circle cx="20" cy="20" r="14" fill="none" stroke="#fff" stroke-width="2"/>
      <path d="M14 12c1-1 2-1 3 0l2 3c.5 1 0 2-1 2.5 1 2 2.5 3.5 4.5 4.5.5-1 1.5-1.5 2.5-1l3 2c1 1 1 2 0 3-2 2-5 2-8-1s-8-7-7-10c0-1 .5-2 1-3z" fill="#fff"/>
    </svg>
    <div class="call-number">01632960418</div>
  </div>

  <div class="abs logo-disc"></div>
  <div class="abs brand">
    <span class="brand-mark"></span>
    <span class="brand-name">BRIGHT PANE<br>HOUSE LTD</span>
  </div>

  <div class="abs social" style="top:30px"></div>
  <div class="abs social" style="top:101px"></div>
  <div class="abs social" style="top:172px"></div>

  <div class="abs window-photo" role="img" aria-label="Photo of a window with teal shutters and pink flower boxes"></div>

  <div class="abs about-tab"></div>
  <div class="abs about-title">ABOUT US</div>
  <p class="abs about-text">Bright Pane House are suppliers and installers of quality windows and doors across Northamptonshire and surrounding villages. Offering a friendly, customer focused approach to your replacement windows and doors.&nbsp; Providing a full colour range of uPVc and aluminium to compliment any home.</p>

  <div class="abs card" style="left:22px;width:213px">
    <div class="card-title">DOORS</div>
    <p class="card-text">We are able to supply &amp; fit Composite Doors, uPVc Doors, French Doors, Bi-Folding Doors, Patio Doors, Stable Doors</p>
  </div>
  <div class="abs card" style="left:247px;width:211px">
    <div class="card-title">WINDOWS</div>
    <p class="card-text">We are able to supply &amp; fit Casement, Tilt and Turn, Vertical Slider/Sash Windows, Bay/Bow Windows, French Windows</p>
  </div>
  <div class="abs card" style="left:470px;width:212px">
    <div class="card-title">REPAIRS</div>
    <p class="card-text">We offer a full repair &amp; replacement service on glass units, windows, &amp; doors. No job is too small for us.</p>
  </div>
  <div class="abs card" style="left:693px;width:213px">
    <div class="card-title">LANDLORD SERVICES</div>
    <p class="card-text">We work closely with Landlords &amp; Letting Agents to offer a full repair/ replacement service glass, windows,doors.</p>
  </div>

  <div class="abs card-ring" style="left:68px">
    <svg width="48" height="70" viewBox="0 0 48 70"><rect x="6" y="2" width="36" height="66" fill="none" stroke="#13258a" stroke-width="4"/><path d="M8 4l24 6v58l-24-2z" fill="#13258a"/><circle cx="27" cy="38" r="2.5" fill="#fff"/></svg>
  </div>
  <div class="abs card-ring" style="left:290px">
    <svg width="48" height="70" viewBox="0 0 48 70"><rect x="3" y="3" width="42" height="64" fill="#13258a"/><g fill="#fff"><rect x="9" y="9" width="13" height="12"/><rect x="26" y="9" width="13" height="12"/><rect x="9" y="25" width="13" height="12"/><rect x="26" y="25" width="13" height="12"/><rect x="9" y="41" width="13" height="12"/><rect x="26" y="41" width="13" height="12"/></g></svg>
  </div>
  <div class="abs card-ring" style="left:514px">
    <svg width="64" height="64" viewBox="0 0 64 64"><g stroke="#13258a" stroke-width="9" stroke-linecap="round"><line x1="12" y1="12" x2="52" y2="52"/><line x1="52" y1="12" x2="14" y2="50"/></g><circle cx="50" cy="14" r="9" fill="#13258a"/><circle cx="53" cy="11" r="4" fill="#fff"/></svg>
  </div>
  <div class="abs card-ring" style="left:737px">
    <svg width="64" height="60" viewBox="0 0 64 60"><path d="M32 4L2 30h8v28h44V30h8z" fill="#13258a"/><rect x="44" y="8" width="8" height="14" fill="#13258a"/><rect x="26" y="38" width="12" height="20" fill="#fff"/></svg>
  </div>

  <div class="abs benefits">
    <div class="abs benefit-col" style="left:20px">✓UK MADE<br>✓10 YEAR GUARANTEE<br>✓REGISTERED INSTALLER</div>
    <div class="abs benefit-col" style="left:285px">✓ADDITIONAL SECURITY<br>✓PRECISION<br>✓FRIENDLY PROFESSIONAL</div>
    <div class="abs benefit-col" style="left:575px">✓COMPETITIVE PRICING<br>✓NO OBLIGATION QUOTES<br>✓A RATED ENERGY EFFICIENT</div>
  </div>

  <div class="abs footer">
    <div class="abs footer-mark"></div>
    <div class="abs footer-address">
      <svg class="abs pin" width="11" height="15" viewBox="0 0 11 15"><path d="M5.5 0A5.5 5.5 0 0 0 0 5.5C0 9.5 5.5 15 5.5 15S11 9.5 11 5.5A5.5 5.5 0 0 0 5.5 0z" fill="#fff"/><circle cx="5.5" cy="5.5" r="2" fill="#1f3c7c"/></svg>
      Bright Pane House Ltd<br>Millbrook House, Canal Road<br>Thornbury, Westshire<br>WS4 7RT
    </div>
    <div class="abs footer-divider"></div>
    <div class="abs footer-contact">
      <svg width="13" height="13" viewBox="0 0 13 13" style="top:3px"><path d="M2 1c1-1 2-1 2.5 0l1.2 2c.3.8-.2 1.3-.8 1.7.8 1.5 2 2.7 3.4 3.4.4-.6 1-1.1 1.7-.8l2 1.2c1 .5 1 1.5 0 2.5-1.5 1.5-4 1-6.5-1.5S.5 2.5 2 1z" fill="#fff"/></svg>
      01632 960 418<br>
      <svg width="13" height="10" viewBox="0 0 13 10" style="top:23px"><rect x=".75" y=".75" width="11.5" height="8.5" fill="none" stroke="#fff" stroke-width="1.5"/><path d="M1 1l5.5 4.5L12 1" fill="none" stroke="#fff" stroke-width="1.5"/></svg>
      sales@brightpanehouse.co.uk<br>
      <svg width="12" height="12" viewBox="0 0 12 12" style="top:40px"><circle cx="6" cy="6" r="5.2" fill="none" stroke="#fff" stroke-width="1.4"/><path d="M1 6h10M6 1c-2.5 3-2.5 7 0 10M6 1c2.5 3 2.5 7 0 10" fill="none" stroke="#fff" stroke-width="1"/></svg>
      www.brightpanehouse.co.uk
    </div>
  </div>
</div>
</body>
</html>
```